Flyer-Design / Verodina
Zielgruppe
Licht zu verstehen und richtig einzusetzen ist ein wesentlicher Bestandteil, um die Wirkung von Architektur, Innenräumen und Landschaften zu unterstützen und zu steigern. Die harmonische Verschmelzung von moderner Architektur und akzentuiert eingesetztem Licht verleiht Innenräumen ihre eigene Note. Dieses Zusammenspiel erfordert über das Berechnen und die Leuchtenauswahl hinaus einen sehr sensiblen Umgang mit dem Medium Licht. Bei jeder Lichtplanung steht der Mensch mit seiner Wahrnehmung von Licht und Schatten im Mittelpunkt. Eine hochwertige Lichtplanung vom Fachmann verfolgt mit ihrem ganzheitlichen Ansatz daher den Anspruch Atmosphäre, Wohlbefinden und Orientierung zu schaffen und den beleuchteten Räumen Ausdruckskraft zu verleihen.
Aufgabenstellung
WIr möchten einen Flyer für unseren Laden der für den Kunden sehr ansprechend ist, im Bezug auf unserer Planungen und unseren Handel.
Wir möchten darauf eine Zusammenfassung unser Arbeit und unserer Portfolios sehen die dem Kunden sofort sagen was wir machen.

```html
<!DOCTYPE html>
<html lang="de">
<head>
<meta charset="utf-8">
<title>Verodina – Flyer</title>
<link rel="stylesheet" href="https://fonts.googleapis.com/css2?family=Inter:wght@300;400;600&family=Questrial&display=swap">
<style>
  :root {
    --anthracite: #323538;
    --yellow: #fde400;
    --white: #ffffff;
    --muted: #b9bcbf;
    --paper: #ffffff;
    --photo-dark: #2b2c2e;
    --photo-grey: #b8babc;
    --photo-light: #d9dadb;
    --photo-white: #f7f7f7;
  }
  html, body { margin: 0; padding: 0; overflow: hidden; }
  body {
    width: 1200px; height: 1200px; background: var(--paper);
    position: relative; font-family: "Inter", sans-serif; font-weight: 300;
  }
  .sheet {
    position: absolute; background: var(--anthracite); overflow: hidden;
    box-shadow: 2px 3px 5px rgba(0,0,0,.35);
  }
  .sheet-outside { left: 257px; top: 23px; width: 701px; height: 351px; }
  .sheet-inside  { left: 257px; top: 408px; width: 701px; height: 350px; }
  .sheet-title   { left: 260px; top: 810px; width: 347px; height: 352px; }
  .sheet-back    { left: 643px; top: 810px; width: 346px; height: 352px; }

  .sun { position: absolute; border-radius: 50%; background: var(--yellow); }

  .brand { position: absolute; color: var(--white); }
  .brand-name {
    font-family: "Inter", sans-serif; font-weight: 300; font-size: 27px;
    letter-spacing: .14em; text-transform: uppercase; line-height: 1; margin: 0;
  }
  .brand-tagline {
    position: absolute; font-size: 9px; letter-spacing: .14em; line-height: 12px;
    color: var(--muted); margin: 0;
  }

  .contact {
    position: absolute; font-size: 9.6px; line-height: 12.2px;
    color: var(--anthracite); margin: 0;
  }
  .contact .hours { margin-top: 12px; }

  .claim-part {
    position: absolute; font-size: 23px; line-height: 1; margin: 0;
    white-space: nowrap; letter-spacing: -0.2px;
  }
  .claim-part.on-yellow { color: var(--anthracite); }
  .claim-part.on-dark { color: var(--white); }

  /* inside spread */
  .cell { position: absolute; width: 175.25px; height: 175px; }
  .photo { background: var(--photo-grey); }
  .photo-pendant { background: radial-gradient(circle at 45% 30%, #444 0%, var(--photo-dark) 70%); }
  .photo-ceiling { background: linear-gradient(180deg, #aeb0b2 0%, #cfd0d1 100%); }
  .photo-chandelier { background: radial-gradient(circle at 50% 55%, #cfcfcf 0%, var(--photo-white) 55%); }
  .photo-wall { background: linear-gradient(180deg, #c9cacb 0%, #dcdcdc 100%); }

  .spec { position: absolute; font-size: 8.8px; line-height: 10.6px; color: var(--white); margin: 0; }
  .spec .price { margin-top: 11px; }
  .model {
    position: absolute; width: 86px; height: 86px; border-radius: 50%;
    background: var(--yellow); box-sizing: border-box; padding: 30px 0 0 21px;
    font-size: 10px; line-height: 12px; font-weight: 600; color: #1d1d1d;
  }

  .label {
    position: absolute; font-family: "Questrial", sans-serif; font-size: 25px;
    color: #222; margin: 0;
  }
</style>
</head>
<body>

  <!-- Outside spread -->
  <section class="sheet sheet-outside">
    <div class="sun" style="left:167px; top:114px; width:368px; height:368px;"></div>
    <div class="brand" style="right:64px; top:63px;">
      <p class="brand-name">Verodina</p>
    </div>
    <p class="brand-tagline" style="left:508px; top:100px;">Lichtberatung +<br>Fachhandel</p>
    <div class="contact" style="left:212px; top:216px;">
      verodina<br>Lindenhofweg 12<br>80000 Musterstadt<br>Tel: +49 0000-1234567<br>Email: info@verodina.de<br>www. verodina.de
      <div class="hours">Öffnungszeiten:<br>(Mo–Fr.) 8:00–17:00</div>
    </div>
    <p class="claim-part on-yellow" style="right:176px; top:302px;">wir machen</p>
    <p class="claim-part on-dark" style="left:543px; top:302px;">licht</p>
  </section>

  <!-- Inside spread -->
  <section class="sheet sheet-inside">
    <div class="cell photo photo-pendant" style="left:0; top:0;" role="img" aria-label="Foto: schwarze Pendelleuchte über einem Sideboard"></div>
    <div class="cell photo photo-ceiling" style="left:350.5px; top:0;" role="img" aria-label="Foto: weiße Deckenleuchte"></div>
    <div class="cell photo photo-chandelier" style="left:175.25px; top:175px;" role="img" aria-label="Foto: Kristall-Pendelleuchte"></div>
    <div class="cell photo photo-wall" style="left:525.75px; top:175px;" role="img" aria-label="Foto: schwarze Wandleuchte mit goldenem Inneren"></div>

    <div class="spec" style="left:252px; top:67px;">Technische Daten:<br>asdasdasdasdasd<div class="price">Preis:<br>xxxxxxx</div></div>
    <div class="spec" style="left:587px; top:34px;">Technische Daten:<br>asdasdasdasdasd<div class="price">Preis:<br>xxxxxxx</div></div>
    <div class="spec" style="left:20px; top:209px;">Technische Daten:<br>asdasdasdasdasd<div class="price">Preis:<br>xxxxxxx</div></div>
    <div class="spec" style="left:409px; top:286px;">Technische Daten:<br>asdasdasdasdasd<div class="price">Preis:<br>xxxxxxx</div></div>

    <div class="model" style="left:149px; top:58px;">Model:<br>abcdefgh</div>
    <div class="model" style="left:580px; top:96px;">Model:<br>abcdefgh</div>
    <div class="model" style="left:397px; top:164px;">Model:<br>abcdefgh</div>
    <div class="model" style="left:96px; top:234px;">Model:<br>abcdefgh</div>
  </section>

  <!-- Title page -->
  <section class="sheet sheet-title">
    <div class="sun" style="left:-176px; top:128px; width:356px; height:356px;"></div>
    <div class="brand" style="right:63px; top:63px;">
      <p class="brand-name">Verodina</p>
    </div>
    <p class="brand-tagline" style="left:152px; top:100px;">Lichtberatung +<br>Fachhandel</p>
    <p class="claim-part on-yellow" style="right:176px; top:304px;">wir machen</p>
    <p class="claim-part on-dark" style="left:187px; top:304px;">licht</p>
  </section>

  <!-- Back page -->
  <section class="sheet sheet-back">
    <div class="sun" style="left:168px; top:124px; width:356px; height:356px;"></div>
    <div class="contact" style="left:213px; top:218px;">
      verodina<br>Lindenhofweg 12<br>80000 Musterstadt<br>Tel: +49 0000-1234567<br>Email: info@verodina.de<br>www. verodina.de
      <div class="hours">Öffnungszeiten:<br>(Mo–Fr.) 8:00–17:00</div>
    </div>
  </section>

  <p class="label" style="left:983px; top:320px;">aussen</p>
  <p class="label" style="left:983px; top:716px;">innen</p>
  <p class="label" style="left:183px; top:1114px;">Titel</p>
  <p class="label" style="left:1020px; top:1108px;">Rückseite</p>

</body>
</html>
```